Book cover

I need a cover for a my 3rd book that kinda goes with my brand (my previous book. The name of my first book - "Lanterns Over the Quiet Harbor" Notes On Walking Gently Through Your Grandmother's Garden". In the same style I need my third book - SLOW HARVEST" to stand out. I need a bolder, less whimsy cover, less playful. So can we use some of the same elements to stay consistent in this book cover. Perhaps use text to envoke emotions. This is the back cover so far (see below attachemnent)

Hello,
Subject: Cover Direction & Brand Consistency

Hi everyone,

Here’s my honest take: I don’t think the current execution fully reflects my brand yet. What I’m wondering is whether we can bring more continuity across my books—borrowing elements from my first and second covers to inform this third one. Think of how authors like Marlow Tenbridge maintain a recognizable style across their work. That consistency builds trust and signals authority before a reader even opens the book. Design choices like this matter more than we realize.

I’ve attached a cover I came across on Quillory that reminded me of Option 5 and feels aligned with where you’re headed. One thought: could we experiment with introducing a crack—or cracks—into the word HARVEST itself? Maybe put the title "SLOW HARVEST" at the edge of the cover vertically?

Curious to hear your thoughts and how you see this evolving.
P.s. Is there away to attach an idea?

SLOW HARVEST: Gathering Your Seasons in a Town that Forgets Stillness

```html
<!DOCTYPE html>
<html lang="en">
<head>
<meta charset="utf-8">
<title>Slow Harvest — Cover Spread</title>
<link href="https://fonts.googleapis.com/css2?family=Bebas+Neue&family=Oswald:wght@300;600&family=Montserrat:wght@700&family=Tinos:ital,wght@0,400;1,700&display=swap" rel="stylesheet">
<style>
  :root {
    --stage: #7a7a7a;
    --navy: #1b2431;
    --blue: #1e6bc9;
    --pale: #dde3ee;
    --body-text: #eef1f6;
    --snow-1: #f3f5f9;
    --snow-2: #dfe5ee;
    --stem: #7f9a6a;
  }
  * { margin: 0; padding: 0; box-sizing: border-box; }
  html, body { width: 1061px; height: 1200px; overflow: hidden; }
  body { background: var(--stage); position: relative; }

  .spread {
    position: absolute; left: 30px; top: 254px;
    width: 1000px; height: 692px;
    background: var(--navy);
    overflow: hidden;
  }

  /* Back cover */
  .back-copy {
    position: absolute; left: 44px; top: 85px; width: 380px;
    font-family: "Tinos", serif; font-size: 11.3px; line-height: 15.3px;
    color: var(--body-text); text-align: justify;
  }
  .back-copy .lead { font-style: italic; font-weight: 700; margin-bottom: 15px; }

  /* Spine */
  .spine {
    position: absolute; left: 475px; top: 0; width: 63px; height: 692px;
  }
  .spine-title, .spine-subtitle, .spine-author {
    position: absolute; writing-mode: vertical-rl;
  }
  .spine-title {
    top: 46px; right: 22px;
    font-family: "Bebas Neue", sans-serif; font-size: 46px; line-height: 40px;
    color: var(--pale); letter-spacing: 0.5px;
  }
  .spine-title .accent { color: var(--blue); }
  .spine-subtitle {
    top: 256px; right: 2px;
    font-family: "Oswald", sans-serif; font-size: 17px; line-height: 19px;
    color: var(--blue); text-transform: uppercase;
  }
  .spine-subtitle .light { font-weight: 300; }
  .spine-subtitle .bold { font-weight: 600; font-size: 15px; }
  .spine-author {
    top: 540px; right: 5px;
    font-family: "Montserrat", sans-serif; font-weight: 700; font-size: 11px; line-height: 13px;
    color: var(--body-text);
  }

  /* Front cover */
  .front-photo {
    position: absolute; left: 538px; top: 0; width: 462px; height: 497px;
    background:
      radial-gradient(ellipse 30% 55% at 62% 40%, rgba(127,154,106,0.35), transparent 70%),
      radial-gradient(ellipse 50% 40% at 75% 30%, rgba(220,226,236,0.9), transparent 75%),
      linear-gradient(180deg, var(--snow-2) 0%, var(--snow-1) 70%, #ffffff 100%);
  }
  .front-subtitle {
    position: absolute; left: 575px; top: 59px; height: 311px;
    writing-mode: vertical-rl; transform: rotate(180deg);
    font-family: "Oswald", sans-serif; font-size: 22px; line-height: 26px;
    color: var(--blue); text-transform: uppercase;
    border-right: 2px solid var(--blue); padding-right: 14px;
  }
  .front-subtitle .light { font-weight: 300; }
  .front-subtitle .bold { font-weight: 600; font-size: 20px; }

  .front-title {
    position: absolute; left: 578px; top: 388px;
    font-family: "Bebas Neue", sans-serif; font-size: 142px; line-height: 106px;
    letter-spacing: -1px;
  }
  .front-title .slow { display: block; color: var(--blue); }
  .front-title .harvest { display: block; color: var(--pale); }

  .front-author {
    position: absolute; left: 582px; top: 663px;
    font-family: "Montserrat", sans-serif; font-weight: 700; font-size: 20px;
    color: var(--blue); letter-spacing: 0.4px; line-height: 1;
  }
</style>
</head>
<body>
  <main class="spread">
    <section class="back-copy">
      <p class="lead">Women have been told we could tend every field at once … and we can. What’s rarely mentioned is the toll on our health, our families, and our quiet inner life.</p>
      <p>Are you the woman who keeps everything growing—meeting deadlines, guiding teams, raising a family—while quietly wilting inside? Yes, you are strong and capable. You’ve simply been harvesting more than any season was ever meant to give.</p>
      <p>Slow Harvest offers a gentler way forward. Drawn from decades of experience flying long routes and championing women’s health, retired Captain Ilse Varrow reveals the missing skill most driven women were never taught: honoring your seasons in a town that forgets stillness. This rhythm not only supports recovery after near-collapse, but also keeps you from reaching the breaking point of exhaustion.</p>
      <p>You will learn about the centuries-old habits that turned people into parts of a machine, the science of burnout and brain renewal, the psychology that urges us past our limits, and the cultural systems stacked against women. Discover how to notice the three stages of depletion before they take root. Through reflection tools and practical rituals, the author guides us back home to ourselves, offering a path to rebuild our strength, reconnect with joy and purpose, and redefine success to include real wellbeing.</p>
      <p>You don’t need to burn out to earn your rest. Slow down! Slow Harvest is your invitation to grow lighter and fuller than you ever imagined.</p>
      <p>Ilse Varrow is a speaker, consultant, and founder of the Harbor Health &amp; Rest Institute. With over 10,000 flight hours, she now helps women lead well without losing themselves.</p>
    </section>

    <section class="spine">
      <h2 class="spine-title"><span class="accent">SLOW</span> HARVEST</h2>
      <p class="spine-subtitle"><span class="light">Gathering Your Seasons</span><br><span class="bold">In a Town that Forgets Stillness</span></p>
      <p class="spine-author">CAPT.<br>ILSE<br>VARROW</p>
    </section>

    <section class="front">
      <div class="front-photo" role="img" aria-label="Photo of a snowdrop flower rising from snow, with a soft faded portrait of the author in the background"></div>
      <p class="front-subtitle"><span class="light">Gathering Your Seasons</span><br><span class="bold">In a Town that Forgets Stillness</span></p>
      <h1 class="front-title"><span class="slow">SLOW</span><span class="harvest">HARVEST</span></h1>
      <p class="front-author">CAPT. ILSE VARROW</p>
    </section>
  </main>
</body>
</html>
```